Upscale business cards needed for family business

We need professional business cards created for several family members. We are a family business holding company. We would like these relatively simple and straightforward, but also with a unique element to set them apart. Probably stick with neutral and simple colors - white, grey etc. We need space for the traditional elements, including name, title, address, email/phone number. And we will be creating several from this template so it needs to be template that is easy to switch information in and out of.

Industry/Entity Type

Business

Contact Information for Business Card

Please include the attached Dunmore Ventures logo.

Requirements
Must have
• The attached Dunmore Ventures logo.

```html
<!DOCTYPE html>
<html lang="en">
<head>
<meta charset="UTF-8">
<title>Dunmore Ventures – Business Cards</title>
<link rel="stylesheet" href="https://fonts.googleapis.com/css2?family=Open+Sans:wght@400;600&display=swap">
<style>
  :root {
    --backdrop: #3b3533;
    --card: #0b0b0b;
    --gold: #f0b81c;
    --text-light: #f2f2f2;
    --text-muted: #d6d6d6;
  }
  * { margin: 0; padding: 0; box-sizing: border-box; }
  html, body {
    width: 1200px;
    height: 900px;
    overflow: hidden;
    background: var(--backdrop);
    font-family: "Open Sans", Arial, sans-serif;
  }
  .canvas {
    position: relative;
    width: 1200px;
    height: 900px;
  }
  .card {
    position: absolute;
    top: 296px;
    width: 540px;
    height: 308px;
    background: var(--card);
    box-shadow: 0 10px 28px rgba(0,0,0,0.45);
  }
  .card--front { left: 40px; }
  .card--back { left: 620px; }

  .brand {
    position: absolute;
    display: flex;
    align-items: center;
    gap: 12px;
    font-weight: 600;
    white-space: nowrap;
  }
  .brand__mark {
    width: 14px;
    height: 14px;
  }
  .card--front .brand {
    left: 60px;
    top: 62px;
    font-size: 34px;
    color: var(--gold);
  }
  .card--front .brand__mark { background: var(--gold); }
  .card--back .brand {
    left: 0;
    right: 0;
    top: 130px;
    justify-content: center;
    font-size: 34px;
    color: var(--text-light);
  }
  .card--back .brand__mark { background: var(--gold); }

  .holder {
    position: absolute;
    left: 60px;
    top: 178px;
    color: var(--text-light);
  }
  .holder__name {
    font-size: 17px;
    font-weight: 600;
    color: var(--gold);
    line-height: 1.2;
  }
  .holder__title {
    font-size: 14px;
    color: var(--text-muted);
    line-height: 1.3;
  }
  .holder__address {
    margin-top: 16px;
    font-size: 15px;
    line-height: 1.35;
    font-style: normal;
  }

  .contact {
    position: absolute;
    left: 300px;
    top: 178px;
    list-style: none;
    color: var(--text-light);
    font-size: 14px;
  }
  .contact__item {
    display: flex;
    align-items: center;
    gap: 10px;
    line-height: 1.6;
  }
  .contact__icon {
    width: 12px;
    height: 12px;
    flex: none;
    fill: var(--gold);
  }
</style>
</head>
<body>
<main class="canvas">

  <section class="card card--front" aria-label="Business card front">
    <div class="brand"><span class="brand__mark"></span>Dunmore Ventures</div>

    <div class="holder">
      <p class="holder__name">Marcus Hale</p>
      <p class="holder__title">Managing Director</p>
      <address class="holder__address">48 Alder Row, Suite 3<br>Greyfield, 40217.</address>
    </div>

    <ul class="contact">
      <li class="contact__item">
        <svg class="contact__icon" viewBox="0 0 12 12" aria-hidden="true"><path d="M2.3 0.8 4 2.6 3.2 4.1c.7 1.5 1.8 2.6 3.3 3.3L8 6.6l1.8 1.7-.9 2.2C5 10.3 1.7 7 1.3 3.1z"/></svg>
        021-555 018 342
      </li>
      <li class="contact__item">
        <svg class="contact__icon" viewBox="0 0 12 12" aria-hidden="true"><path d="M1 2.5h10v7H1z M1 2.5 6 6.5 11 2.5" stroke="#0b0b0b" stroke-width="0.8"/></svg>
        hello@dunmoreventures.co
      </li>
      <li class="contact__item">
        <svg class="contact__icon" viewBox="0 0 12 12" aria-hidden="true"><circle cx="6" cy="6" r="5.5"/><path d="M0.5 6h11M6 0.5c-2.2 2.8-2.2 8.2 0 11M6 0.5c2.2 2.8 2.2 8.2 0 11" stroke="#0b0b0b" stroke-width="0.7" fill="none"/></svg>
        www.dunmoreventures.co
      </li>
    </ul>
  </section>

  <section class="card card--back" aria-label="Business card back">
    <div class="brand"><span class="brand__mark"></span>Dunmore Ventures</div>
  </section>

</main>
</body>
</html>
```